Brightpath Wellness Institute needs a patient engagement brochure thats eye catching and useful

a patient engagement brochure to move patient to discover their diabetes and to seek help with us. The flyer should be cheerful and welcoming and have a feeling of hope. Animated people and figures may be used to convey this feeling.

Target Market(s)

Patients living with diabetes over 40 years old

Industry/Entity Type

Medical

Colors
fee18a
f68d4c
cadf82

Requirements
Must have
• Bright colors of hope. None corporate look. Like to leave it a trifold. I need to incorporate all text on onside of the flier and better designed food log on the other side.
Nice to have
• Possible using animation,

```html
<!DOCTYPE html>
<html lang="en">
<head>
<meta charset="utf-8">
<title>Discover Your Diabetes – Brightpath Wellness Institute</title>
<link rel="stylesheet" href="https://fonts.googleapis.com/css2?family=Oswald:wght@500;700&family=Open+Sans:ital,wght@0,400;0,600;0,700;0,800;1,400;1,600&display=swap">
<style>
:root{
  --orange:#f68d4c;
  --orange-deep:#ee6a1f;
  --yellow:#fee18a;
  --green:#cadf82;
  --green-deep:#9fc24a;
  --ink:#2b2b2b;
  --dark:#1e1e1e;
  --red:#d8262b;
  --paper:#ffffff;
  --stage:#e4e4e4;
  --line:#3a3a3a;
}
*{box-sizing:border-box;margin:0;padding:0}
html,body{width:1061px;height:1200px;overflow:hidden;background:var(--stage)}
body{position:relative;font-family:"Open Sans",Arial,sans-serif;color:var(--ink)}

.sheet{position:absolute;left:130px;width:800px;background:var(--paper);box-shadow:0 2px 8px rgba(0,0,0,.18);overflow:hidden}
.outside{top:20px;height:566px}
.record{top:604px;height:576px;padding:22px 30px}

.panel{position:absolute;top:0;height:566px}
.panel-inside{left:0;width:265px;background:linear-gradient(180deg,#d6e896 0%,var(--green) 45%,#b5d26a 100%);padding:18px 14px 10px}
.panel-middle{left:265px;width:267px}
.panel-cover{left:532px;width:268px}

/* left panel */
.tool-banner{position:relative;margin:0 -14px 8px;background:var(--orange);color:#fff;font-family:"Oswald",sans-serif;font-weight:500;font-size:9.5px;line-height:1.2;text-align:center;padding:5px 20px;clip-path:polygon(0 0,100% 0,94% 100%,0 100%)}
.tool-banner strong{display:block;font-size:11px;font-weight:700}
.steps{font-size:6.3px;line-height:1.33;color:#2f3a12}
.steps h3{font-family:"Oswald",sans-serif;font-weight:500;font-size:7.3px;color:#fff;margin:3px 0 1px}
.steps h4{font-size:6.6px;font-weight:700;margin:2px 0 1px}
.steps p{margin-bottom:2px}
.steps b{font-weight:700}
.steps u{font-weight:600}
.footnotes{display:flex;gap:10px;margin-top:8px;font-size:4.8px;line-height:1.3;color:var(--orange-deep)}
.footnotes span{flex:1}

/* middle panel */
.photo{position:absolute;background:linear-gradient(160deg,#e7d6c6,#8c6a52 70%,#5a4636)}
.doctor-photo{position:absolute;left:34px;top:8px;width:86px;height:86px;border-radius:50%;border:4px solid var(--green);background:radial-gradient(circle at 50% 40%,#f5f5f5 0 30%,#cfd6dd 60%,#a9b3bd)}
.can-do-banner{position:absolute;left:0;top:135px;width:245px;height:20px;background:var(--yellow);clip-path:polygon(0 0,92% 0,100% 100%,0 100%);font-family:"Oswald",sans-serif;font-weight:500;font-size:8px;line-height:20px;padding-left:14px;color:var(--ink)}
.can-do{position:absolute;left:14px;top:164px;width:228px;font-size:6.3px;line-height:1.38}
.can-do .lead{color:var(--orange-deep);font-weight:600;margin-bottom:5px}
.can-do ul{list-style:none}
.can-do li{position:relative;padding-left:10px;margin-bottom:5px}
.can-do li::before{content:"";position:absolute;left:0;top:2px;width:4px;height:4px;border-radius:50%;background:var(--ink)}
.can-do b{font-weight:700}
.can-do .closing{margin-top:10px}
.contact{position:absolute;left:14px;top:375px;width:228px;display:flex;justify-content:space-between;font-size:6px;line-height:1.4}
.brand{display:flex;align-items:center;gap:4px;font-family:"Open Sans",sans-serif;font-weight:700;color:var(--red);white-space:nowrap}
.brand::after{content:"";width:8px;height:8px;border-radius:50%;background:var(--red)}
.contact .brand{font-size:7px;margin-bottom:3px}
.map{position:absolute;left:14px;top:410px;width:190px;height:62px;background:linear-gradient(180deg,#f2f2f2,#dcdcdc)}
.web{position:absolute;left:0;right:0;bottom:14px;text-align:center;color:#fff;font-weight:600;font-size:10.5px;letter-spacing:.3px}

/* cover panel */
.couple-photo{left:0;top:0;width:268px;height:132px;background:linear-gradient(200deg,#f6c66a 0%,#e08a2c 35%,#7a4a24 75%,#3c2818)}
.cover-brand{position:absolute;left:96px;top:174px;font-size:8.5px}
.title-band{position:absolute;left:-8px;top:198px;width:276px;height:98px;background:linear-gradient(180deg,#f89b5c,var(--orange-deep));padding:10px 0 0 30px;font-family:"Oswald",sans-serif;font-weight:700;line-height:1}
.title-band .top{display:block;color:#fff;font-size:26px;letter-spacing:.4px}
.title-band .big{display:block;color:var(--dark);font-size:44px;letter-spacing:.5px;margin-top:3px}
.questions{position:absolute;left:28px;top:322px;width:225px;list-style:none;font-family:"Oswald",sans-serif;font-weight:500;font-size:8.3px;line-height:1.35;color:var(--ink)}
.questions li{position:relative;padding-left:12px;margin-bottom:6px}
.questions li::before{content:"";position:absolute;left:0;top:4px;width:4px;height:4px;border-radius:50%;background:var(--red)}
.tagline{position:absolute;left:0;width:268px;top:442px;text-align:center;font-family:"Oswald",sans-serif;font-weight:500;font-size:10.5px;line-height:1.3;color:var(--orange-deep)}

.deco{position:absolute;left:0;top:0;pointer-events:none}

/* record form */
.form-head{display:flex;justify-content:space-between;align-items:flex-end;font-size:9px;font-weight:600;margin-bottom:6px}
.form-head .name span{display:inline-block;width:210px;border-bottom:1px solid var(--ink);margin-left:4px}
.form-head .form-title{font-style:italic;font-weight:600}
.log{width:740px;height:418px;border:3px solid var(--line);border-radius:12px;overflow:hidden;display:grid;
  grid-template-columns:36px 32px 85px 32px 32px 88px 32px 33px 90px 32px 33px 32px 87px 86px;
  grid-template-rows:76px repeat(7,1fr) 18px;background:var(--line);gap:0}
.cell{border-right:1px solid #fff3a0;border-bottom:1px solid #fff3a0}
.cell.o{background:linear-gradient(90deg,#f47a2c,#f9a061 50%,#f47a2c)}
.cell.g{background:linear-gradient(90deg,#9fc24a,#d6ea96 50%,#9fc24a)}
.cell.h{display:flex;flex-direction:column;align-items:center;justify-content:flex-start;padding-top:8px;font-family:"Oswald",sans-serif;font-weight:500;font-size:6.2px;line-height:1.15;text-align:center;color:var(--dark);border-bottom:2px solid #fff3a0}
.cell.h i{display:block;width:14px;height:10px;border-radius:3px;background:var(--dark);margin-bottom:3px}
.cell.avg{font-family:"Oswald",sans-serif;font-size:6px;color:var(--dark);padding:4px 0 0 4px}
.form-foot{display:flex;justify-content:space-between;margin-top:10px;font-size:8px;line-height:1.35}
.form-foot .note{color:var(--orange-deep);margin-bottom:3px}
.form-foot h5{font-family:"Oswald",sans-serif;font-weight:700;font-size:9px;letter-spacing:.4px}
.form-foot .credit{text-align:center;padding-right:40px}
.form-foot .credit em{font-style:italic}
</style>
</head>
<body>

<section class="sheet outside">

  <div class="panel panel-inside">
    <div class="tool-banner">HOW TO MAKE BLOOD GLUCOSE CHECKS YOUR <strong>"TOOL OF DISCOVERY"</strong></div>
    <div class="steps">
      <h3>STEP 1: DECIDE TO DO IT</h3>
      <p>If you are not sure why you should, read the What BWI Discovery Can Do for You section of this brochure.</p>
      <h3>STEP 2: GATHER INFORMATION</h3>
      <p>Use the record form on the back to gather detailed information about your diabetes for at least 3-4 days. Repeat as needed. In addition to your BS's (Blood sugars), record the things that contribute to the results, such as what you eat, your medicines, exercise, and illness or stress. Go about your usual life. Eat the foods you enjoy and normally eat in amounts normal for you. This is how to learn the most about your diabetes – to see what is working and what is not.</p>
      <h4>Make Sure It Is the Right Information</h4>
      <p>BS's at different times give different information. In combination, they can show exactly how both your treatment and your own actions affect your BS.</p>
      <p><u>Fasting &amp; before meal checks</u> tell you if you have enough insulin* to control BS when you are NOT eating. They are also the starting point for seeing the effect of what you eat.</p>
      <p><u>After meal checks</u> show you if your insulin* matched what you ate.</p>
      <p><u>Bedtime and nighttime checks</u> show the pattern of BS's over night and can reveal unrecognized lows.</p>
      <p><u>Checks before driving or exercising</u> can show when you are at risk of lows or high blood sugar.<br>When you have your records, move on to Step 3.</p>
      <h3>STEP 3: USE WHAT YOU FIND</h3>
      <p>Once you Discover a problem, take steps to correct it. As each problem is fixed, your overall control will improve.</p>
      <p><b>Start with the Morning Fasting</b> – If your BS averages over 100 before breakfast, especially if it rises over night, it can mean your body is releasing extra sugar at night. This problem is best treated with medicines. See your doctor. Starting high each morning makes it hard to control BS the rest of the day.</p>
      <p><b>Highs Before Other Meals</b> – If your BS averages above 100 before lunch or dinner after the morning fasting has been fixed, check to see if the BS two hours after the previous meal was too high also. If so, work on that.</p>
      <p><b>Look at Each Meal</b> – If your BS rises more than 50 points when you eat, it means there was not enough insulin* to match what you ate. Consider reducing carbohydrate to better match insulin*. This makes most sense if you are eating more than 45-60 grams of carb** at a meal. If your BG rises over 50 points when you eat less than 45-60 grams, your mealtime insulin* levels are too low. Talk to your doctor about adjusting medicines or doses. If after meal BS stays high, A1c will be above target.</p>
      <p><b>If You Find Lows</b> – BS of 70 or less means there was too much insulin* for the current need. This can happen if you delay or skip a meal or snack or you are more active. If that was not the case, your medicines may need adjustment.</p>
    </div>
    <div class="footnotes">
      <span>*made by your body or from injections</span>
      <span>** If you do not know how to identify and count carbohydrate foods, ask your doctor for a referral to a diabetes educator.</span>
    </div>
  </div>

  <div class="panel panel-middle">
    <svg class="deco" width="267" height="566" viewBox="0 0 267 566" aria-hidden="true">
      <path d="M0 118 C70 100 170 96 267 126" stroke="var(--green)" stroke-width="3" fill="none"/>
      <path d="M0 124 C80 108 170 106 267 134" stroke="var(--yellow)" stroke-width="2" fill="none"/>
      <path d="M0 500 C90 482 180 484 267 506 L267 566 L0 566Z" fill="var(--orange-deep)"/>
      <path d="M0 492 C90 474 180 476 267 498" stroke="var(--green)" stroke-width="3" fill="none"/>
    </svg>
    <div class="doctor-photo" role="img" aria-label="Portrait photo of a smiling doctor giving a thumbs up"></div>
    <div class="can-do-banner">WHAT BWI DISCOVERY CAN DO FOR YOU</div>
    <div class="can-do">
      <p class="lead">Few people achieve the blood sugar (BS) targets that experts recommend. There are many reasons for this, including:</p>
      <ul>
        <li><b>Getting general information about diabetes</b>, not specific advice about how to manage diabetes in their own life – their foods, their medicines, and their priorities.</li>
        <li><b>Gathering just the numbers when they test.</b> When they or their doctor review the numbers, they do not know the conditions surrounding each number. If you do not know exactly what produced a number, you cannot know what to do to make it better.</li>
        <li><b>Testing too little to discover</b> patterns &amp; relationships.</li>
      </ul>
      <p class="closing">With the BWI Discovery process, you can learn exactly how your diabetes works and take specific actions to reach your goals. No more testing without improvement. And no more living in the "diabetes cookie cutter box." Call us to register for our next diabetes program.</p>
    </div>
    <div class="contact">
      <div>1420 Maple Ridge Rd<br>Lakeview, CA 90001<br>880 Orchard Blvd Ste 200<br>Fairhaven, CA 90010</div>
      <div>
        <div class="brand">Brightpath Wellness Institute</div>
        Phone: 555-014-0111<br>Toll Free: 1-800-555-0199
      </div>
    </div>
    <div class="map" role="img" aria-label="Street map showing the two clinic locations"></div>
    <div class="web">www.brightpathwellness.org</div>
  </div>

  <div class="panel panel-cover">
    <div class="photo couple-photo" role="img" aria-label="Photo of an older couple embracing in a field at sunset"></div>
    <svg class="deco" width="268" height="566" viewBox="0 0 268 566" aria-hidden="true">
      <path d="M0 118 C80 150 180 150 268 112 L268 566 L0 566Z" fill="#fff"/>
      <path d="M0 122 C80 156 180 156 268 118" stroke="var(--green)" stroke-width="3" fill="none"/>
      <path d="M0 130 C80 164 180 164 268 126" stroke="var(--yellow)" stroke-width="2" fill="none"/>
      <path d="M0 522 C90 504 180 504 268 518 L268 566 L0 566Z" fill="var(--orange-deep)"/>
      <path d="M0 514 C90 496 180 496 268 510" stroke="var(--green)" stroke-width="3" fill="none"/>
    </svg>
    <div class="brand cover-brand">Brightpath Wellness Institute</div>
    <div class="title-band"><span class="top">DISCOVER YOUR</span><span class="big">DIABETES</span></div>
    <ul class="questions">
      <li>ARE YOU FRUSTRATED BY TESTING YOUR BLOOD SUGAR BUT SEEING NO IMPROVEMENT?</li>
      <li>DO YOU FEEL LIKE YOUR LIFE DOESN'T FIT IN THE "DIABETES COOKIE CUTTER BOX?"</li>
      <li>THEN USE THIS SIMPLE TOOL TO DISCOVER HOW YOUR DIABETES ACTUALLY WORKS.</li>
    </ul>
    <p class="tagline">A Guide for New and Experienced People<br>Living with Diabetes</p>
    <div class="web">www.brightpathwellness.org</div>
  </div>
</section>

<section class="sheet record">
  <div class="form-head">
    <div class="name">Name:<span></span></div>
    <div class="form-title">Discovery Record Form</div>
  </div>
  <div class="log">
    <div class="cell o h">DATE</div>
    <div class="cell g h">FASTING BLOOD SUGAR (FBS)</div>
    <div class="cell o h"><i></i>BREAKFAST FOODS EATEN</div>
    <div class="cell g h">1-2 HR BLOOD SUGAR</div>
    <div class="cell g h">BEFORE LUNCH BLOOD SUGAR</div>
    <div class="cell o h"><i></i>LUNCH FOODS EATEN</div>
    <div class="cell g h">1-2 HR BLOOD SUGAR</div>
    <div class="cell g h">BEFORE DINNER BLOOD SUGAR</div>
    <div class="cell o h"><i></i>DINNER FOODS EATEN</div>
    <div class="cell g h">1-2 HR BLOOD SUGAR</div>
    <div class="cell g h">BEDTIME BLOOD SUGAR</div>
    <div class="cell g h">*3AM BLOOD SUGAR</div>
    <div class="cell o h"><i></i>EXERCISE TODAY</div>
    <div class="cell o h"><i></i>SPECIAL COMMENTS</div>

    <div class="cell o"></div><div class="cell g"></div><div class="cell o"></div><div class="cell g"></div><div class="cell g"></div><div class="cell o"></div><div class="cell g"></div><div class="cell g"></div><div class="cell o"></div><div class="cell g"></div><div class="cell g"></div><div class="cell g"></div><div class="cell o"></div><div class="cell o"></div>
    <div class="cell o"></div><div class="cell g"></div><div class="cell o"></div><div class="cell g"></div><div class="cell g"></div><div class="cell o"></div><div class="cell g"></div><div class="cell g"></div><div class="cell o"></div><div class="cell g"></div><div class="cell g"></div><div class="cell g"></div><div class="cell o"></div><div class="cell o"></div>
    <div class="cell o"></div><div class="cell g"></div><div class="cell o"></div><div class="cell g"></div><div class="cell g"></div><div class="cell o"></div><div class="cell g"></div><div class="cell g"></div><div class="cell o"></div><div class="cell g"></div><div class="cell g"></div><div class="cell g"></div><div class="cell o"></div><div class="cell o"></div>
    <div class="cell o"></div><div class="cell g"></div><div class="cell o"></div><div class="cell g"></div><div class="cell g"></div><div class="cell o"></div><div class="cell g"></div><div class="cell g"></div><div class="cell o"></div><div class="cell g"></div><div class="cell g"></div><div class="cell g"></div><div class="cell o"></div><div class="cell o"></div>
    <div class="cell o"></div><div class="cell g"></div><div class="cell o"></div><div class="cell g"></div><div class="cell g"></div><div class="cell o"></div><div class="cell g"></div><div class="cell g"></div><div class="cell o"></div><div class="cell g"></div><div class="cell g"></div><div class="cell g"></div><div class="cell o"></div><div class="cell o"></div>
    <div class="cell o"></div><div class="cell g"></div><div class="cell o"></div><div class="cell g"></div><div class="cell g"></div><div class="cell o"></div><div class="cell g"></div><div class="cell g"></div><div class="cell o"></div><div class="cell g"></div><div class="cell g"></div><div class="cell g"></div><div class="cell o"></div><div class="cell o"></div>
    <div class="cell o"></div><div class="cell g"></div><div class="cell o"></div><div class="cell g"></div><div class="cell g"></div><div class="cell o"></div><div class="cell g"></div><div class="cell g"></div><div class="cell o"></div><div class="cell g"></div><div class="cell g"></div><div class="cell g"></div><div class="cell o"></div><div class="cell o"></div>

    <div class="cell o avg">AVG</div><div class="cell g"></div><div class="cell o"></div><div class="cell g"></div><div class="cell g"></div><div class="cell o"></div><div class="cell g"></div><div class="cell g"></div><div class="cell o"></div><div class="cell g"></div><div class="cell g"></div><div class="cell g"></div><div class="cell o"></div><div class="cell o"></div>
  </div>
  <div class="form-foot">
    <div>
      <p class="note">* If you suspect or experience lows in the night</p>
      <h5>RECOMMENDED AVERAGE BLOOD SUGAR TARGETS:</h5>
      <p>- before meals, less than 110 mg/dl</p>
      <p>- 2 hours after meals, less than 140 mg/dl</p>
    </div>
    <div class="credit">
      <p>©Brightpath Wellness Institute Diabetes Management &amp; Training Centers, 2015</p>
      <p><em>"Where people learn to make a difference"</em></p>
    </div>
  </div>
</section>

</body>
</html>
```